Wine Label for a Prosecco Wine Called Tavi

Prosecco is a white sparkling wine from Italy. We are looking for an eye catching, elegant label for this prosecco that is called "Tavi" because it is a young, fresh, lively white sparkling wine. (We do not want to see children or babies featured on the label-- just the name TAVI please.) Attached is the old label for your reference, and the bottle type that will be used , which is a dark green Burgundy style bottle (pls ignore the label on the bottle). Please no grapes or wine glasses on the label. We are looking for something: eye catching / fun / ELEGANT (not cheap). We would be happy with a fun color too. Remember-- elegant, eye catching! Thanks!
Updates

Hi All, I think I made a mistake in my brief and have updated it. I also uploaded a competitor's label that we like very much to give better direction to what we are looking for. Also, the word Tavi cannot be vertical, nor can it be broken. It needs to read: TAVI or Tavi. Thanks

Target Market(s)

American adults male and female.

Colors
abd036
33a6d7
33b8a4
ffcf3e

Requirements
Must have
• The mandatory information as shown on old labels. The word TAVI should be very prominent.
Nice to have
• The uploaded photo of a competitor's prosecco shows a label we really like... if you could play around with this shape and style we'd be very happy.
Should not have
• No grape images, no wine glass images, no images of babies or children.

```html
<!DOCTYPE html>
<html lang="it">
<head>
<meta charset="utf-8">
<title>Tavi Prosecco Frizzante – Label</title>
<link href="https://fonts.googleapis.com/css2?family=Cinzel:wght@400;500&family=Cormorant+Garamond:wght@500;600&display=swap" rel="stylesheet">
<style>
  :root {
    --page: #ffffff;
    --cream: #fdfbe2;
    --gold: #a47a2c;
    --gold-light: #e2bd5c;
    --gold-dark: #7a5418;
    --ink: #1c1a16;
    --swirl-blue: #2f8fd0;
    --swirl-navy: #1d3f8a;
    --swirl-cyan: #4cc6dc;
    --swirl-red: #e0344a;
    --swirl-orange: #f08a2c;
    --swirl-yellow: #f6c44a;
    --swirl-magenta: #b8336e;
  }
  * { margin: 0; padding: 0; box-sizing: border-box; }
  html, body {
    width: 1200px; height: 1200px; overflow: hidden;
    background: var(--page);
  }
  .canvas {
    position: relative; width: 1200px; height: 1200px;
  }
  .label {
    position: absolute; left: 165px; top: 150px;
    width: 870px; height: 900px;
    overflow: hidden;
  }
  .label__artwork {
    position: absolute; inset: 0;
    background:
      radial-gradient(ellipse 45% 30% at 25% 15%, var(--swirl-blue) 0%, transparent 70%),
      radial-gradient(ellipse 40% 28% at 75% 12%, var(--swirl-cyan) 0%, transparent 70%),
      radial-gradient(ellipse 30% 25% at 10% 45%, var(--swirl-magenta) 0%, transparent 70%),
      radial-gradient(ellipse 35% 30% at 85% 45%, var(--swirl-red) 0%, transparent 70%),
      radial-gradient(ellipse 45% 30% at 55% 85%, var(--swirl-yellow) 0%, transparent 70%),
      radial-gradient(ellipse 35% 30% at 20% 80%, var(--swirl-orange) 0%, transparent 70%),
      radial-gradient(ellipse 30% 30% at 95% 85%, var(--swirl-cyan) 0%, transparent 70%),
      linear-gradient(170deg, var(--swirl-navy) 0%, var(--swirl-blue) 30%, var(--swirl-red) 55%, var(--swirl-orange) 80%, var(--swirl-yellow) 100%);
  }
  .label__panel {
    position: absolute; left: 223px; top: 252px;
    width: 423px; height: 396px;
    background: var(--cream);
  }
  .label__frame {
    position: absolute; inset: 24px;
    border: 2px solid var(--gold);
    display: flex; flex-direction: column; align-items: center;
    text-align: center;
  }
  .label__name {
    margin-top: 22px;
    font-family: "Cinzel", serif; font-weight: 400;
    font-size: 118px; line-height: 1;
    letter-spacing: 0.02em;
    color: var(--gold);
  }
  .label__wine {
    margin-top: 22px;
    font-family: "Cormorant Garamond", serif; font-weight: 600;
    font-size: 32px; letter-spacing: 0.42em;
    margin-right: -0.42em;
    color: var(--ink);
  }
  .label__origin {
    margin-top: 20px;
    font-family: "Cormorant Garamond", serif; font-weight: 500;
    font-size: 17px; line-height: 1.35; letter-spacing: 0.2em;
    margin-right: -0.2em;
    color: var(--ink);
  }
  .label__style {
    margin-top: 18px;
    font-family: "Cormorant Garamond", serif; font-weight: 600;
    font-size: 27px; letter-spacing: 0.48em;
    margin-right: -0.48em;
    color: var(--ink);
  }
</style>
</head>
<body>
  <main class="canvas">
    <section class="label">
      <div class="label__artwork" role="img" aria-label="Marbled swirling paint pattern in blue, turquoise, red, orange and yellow"></div>
      <div class="label__panel">
        <div class="label__frame">
          <h1 class="label__name">TAVI</h1>
          <p class="label__wine">PROSECCO</p>
          <p class="label__origin">DENOMINAZIONE DE<br>ORIGINE CONTROLLATA</p>
          <p class="label__style">FRIZZANTE</p>
        </div>
      </div>
    </section>
  </main>
</body>
</html>
```